Information Systems Internal Communication Brochure

We need a brochure that we can use as an internal marketing tool to highlight a number of the information technology projects we are working on across our business.

Looking for flat UI style design elements, needs to have four sections that cater for IT servers/storage/desktops, GIS (Mapping - Think Plovix Orbit), Information Management and General Corporate Applications/Software.

Included in the files is the logo which needs to be incorporated into the design at the top right hand corner. Colours can also be used throughout if required.

The brochure needs to be easily editable by people with limited graphic design skills, and the graphics easily changeable to suit different projects.

```html
<!DOCTYPE html>
<html lang="en">
<head>
<meta charset="utf-8">
<title>Information Systems – Projects Brochure</title>
<link rel="stylesheet" href="https://fonts.googleapis.com/css2?family=Questrial&display=swap">
<style>
  :root {
    --paper: #ffffff;
    --band: #0b2d3a;
    --bar: #4cc6ef;
    --disc: #0fa8d8;
    --ring: #ffffff;
    --ink-light: #ffffff;
    --brand: #1d6fa3;
    --font: "Questrial", "Century Gothic", sans-serif;
  }
  * { box-sizing: border-box; margin: 0; padding: 0; }
  html, body { width: 1200px; height: 840px; overflow: hidden; background: var(--paper); }
  .brochure {
    position: relative;
    width: 1200px;
    height: 840px;
    background: var(--paper);
    font-family: var(--font);
    overflow: hidden;
  }
  .brochure__band {
    position: absolute;
    left: 0; right: 0; bottom: 0;
    height: 330px;
    background: var(--band);
  }
  .brand {
    position: absolute;
    left: 40px; top: 44px;
    display: flex;
    align-items: center;
    gap: 12px;
    color: var(--brand);
  }
  .brand__mark {
    width: 30px; height: 30px;
    border-radius: 50%;
    background: var(--brand);
    flex: none;
  }
  .brand__name {
    font-size: 18px;
    line-height: 1.2;
    letter-spacing: 0.04em;
    text-transform: uppercase;
    font-weight: 400;
  }
  .service {
    position: absolute;
    top: 30px;
    width: 150px;
    height: 550px;
  }
  .service__bar {
    position: absolute;
    left: 62px; top: 0;
    width: 70px;
    height: 500px;
    background: var(--bar);
    display: flex;
    justify-content: center;
  }
  .service__label {
    writing-mode: vertical-rl;
    transform: rotate(180deg);
    color: var(--ink-light);
    font-size: 20px;
    font-weight: 400;
    line-height: 1.2;
    padding: 90px 0 12px;
    white-space: nowrap;
  }
  .service__badge {
    position: absolute;
    left: 0; bottom: 0;
    width: 140px; height: 140px;
    border-radius: 50%;
    background: var(--disc);
    border: 5px solid var(--ring);
    display: flex;
    align-items: center;
    justify-content: center;
  }
  .service__icon { width: 74px; height: 74px; }
  .service--infrastructure { left: 260px; }
  .service--information   { left: 490px; }
  .service--gis           { left: 720px; }
  .service--applications  { left: 950px; }
</style>
</head>
<body>
<main class="brochure">
  <div class="brochure__band"></div>

  <header class="brand">
    <span class="brand__mark"></span>
    <span class="brand__name">Harbourvale<br>Regional Council</span>
  </header>

  <section class="service service--infrastructure">
    <div class="service__bar"><h2 class="service__label">IT Servers/Storage/Desktops</h2></div>
    <div class="service__badge">
      <svg class="service__icon" viewBox="0 0 74 74" fill="none" stroke="#fff" stroke-width="2.5">
        <rect x="6" y="30" width="30" height="34"/>
        <line x1="10" y1="38" x2="32" y2="38"/><line x1="10" y1="46" x2="32" y2="46"/><line x1="10" y1="54" x2="32" y2="54"/>
        <rect x="40" y="20" width="28" height="22"/>
        <line x1="54" y1="42" x2="54" y2="50"/><line x1="46" y1="50" x2="62" y2="50"/>
        <path d="M24 22a6 6 0 0 1 10-5a5 5 0 0 1 8 4h-18z" fill="#fff"/>
      </svg>
    </div>
  </section>

  <section class="service service--information">
    <div class="service__bar"><h2 class="service__label">Information Management</h2></div>
    <div class="service__badge">
      <svg class="service__icon" viewBox="0 0 74 74" fill="none" stroke="#fff" stroke-width="2.5">
        <rect x="26" y="8" width="22" height="28" fill="#fff"/>
        <rect x="40" y="14" width="22" height="28" fill="#fff"/>
        <rect x="12" y="16" width="22" height="26" fill="#fff"/>
        <circle cx="28" cy="56" r="11"/>
        <line x1="28" y1="53" x2="28" y2="61"/><circle cx="28" cy="49.5" r="0.8" fill="#fff"/>
      </svg>
    </div>
  </section>

  <section class="service service--gis">
    <div class="service__bar"><h2 class="service__label">GIS (Geographical Information System)</h2></div>
    <div class="service__badge">
      <svg class="service__icon" viewBox="0 0 74 74" fill="none" stroke="#fff" stroke-width="2.5">
        <circle cx="37" cy="37" r="30"/>
        <ellipse cx="37" cy="37" rx="13" ry="30"/>
        <line x1="37" y1="7" x2="37" y2="67"/>
        <line x1="7" y1="37" x2="67" y2="37"/>
        <path d="M12 22h50M12 52h50"/>
      </svg>
    </div>
  </section>

  <section class="service service--applications">
    <div class="service__bar"><h2 class="service__label">General Corporate Applications<br>/Software</h2></div>
    <div class="service__badge">
      <svg class="service__icon" viewBox="0 0 74 74" fill="none" stroke="#fff" stroke-width="2.5">
        <rect x="28" y="8" width="18" height="22" fill="#fff" transform="rotate(-12 37 19)"/>
        <rect x="38" y="12" width="18" height="22" fill="#fff"/>
        <circle cx="26" cy="50" r="14" fill="#fff"/>
        <circle cx="48" cy="50" r="14" fill="#fff"/>
        <circle cx="26" cy="50" r="3" fill="#0fa8d8" stroke="none"/>
        <circle cx="48" cy="50" r="3" fill="#0fa8d8" stroke="none"/>
      </svg>
    </div>
  </section>
</main>
</body>
</html>
```